Granite Valley Supply Works, LLC

Would like an e-commerce website started

north-fork gaskets website is a business that is almost exactly like ours...I like how in the front of the website...their lines flash across the bottom...I have attached our line card to add some of ours

we are trel certified...I would like that to show...... attached logo

also attached our logo

```html
<!DOCTYPE html>
<html lang="en">
<head>
<meta charset="utf-8">
<title>Granite Valley Supply Works, LLC — Homepage Concepts</title>
<link rel="stylesheet" href="https://fonts.googleapis.com/css2?family=Montserrat:wght@500;600;700&family=Roboto:wght@400;500;700&display=swap">
<style>
:root{
  --green:#5b9a2a;--green-d:#4b8420;--yellow:#f5b800;--ink:#1d1d1d;--muted:#8a8a8a;
  --light:#f3f3f3;--cream:#fffbea;--black:#121212;--canvas:#a9a9a9;--field:#ececec;--white:#fff;
}
*{box-sizing:border-box;margin:0;padding:0}
html,body{width:1200px;height:2464px;overflow:hidden}
body{background:var(--canvas);font-family:Roboto,Arial,sans-serif;color:var(--ink);position:relative}
.page{position:absolute;top:66px;width:514px;background:var(--white);overflow:hidden}
.page--a{left:60px;height:2069px}
.page--b{left:625px;height:2332px}
.sec{position:absolute;left:0;width:514px;overflow:hidden}
.abs{position:absolute}
.center{left:0;width:514px;text-align:center}
/* header */
.topbar{top:0;height:15px;background:var(--canvas)}
.topbar-strip{position:absolute;right:0;top:0;width:325px;height:15px;background:#dcdcdc;clip-path:polygon(14px 0,100% 0,100% 100%,0 100%);font-size:4.6px;color:#555;display:flex;align-items:center;padding-left:30px}
.topbar-strip .gold{color:#c98f00;margin-right:10px}
.topbar-strip .auth{margin-left:auto;margin-right:14px}
.header{top:15px;height:27px;background:var(--white);box-shadow:0 1px 2px rgba(0,0,0,.08);z-index:3}
.brand{position:absolute;left:61px;top:5px;display:flex;align-items:center;gap:3px}
.brand-box{width:9px;height:17px;background:var(--ink)}
.brand-name{font:600 6px/1.15 Montserrat,sans-serif;color:var(--ink);width:76px}
.nav{position:absolute;left:165px;top:11px;display:flex;gap:9px;font-size:5.6px;color:var(--ink)}
.nav svg{width:6px;height:6px}
/* hero */
.hero{top:42px;height:270px}
.hero-photo{position:absolute;inset:0}
.hero-photo--factory{background:linear-gradient(100deg,#23303f 0%,#3a4656 35%,#5c5a4a 60%,#9a7d2c 80%,#3c4048 100%)}
.hero-photo--warehouse{background:linear-gradient(180deg,#2a2119 0%,#5a3f28 40%,#7a5636 70%,#a48464 100%)}
.hero-shade{position:absolute;inset:0;background:rgba(0,0,0,.25)}
.welcome{font:600 7px Montserrat,sans-serif;color:var(--yellow)}
.hero-title{font:600 15.5px Montserrat,sans-serif;color:var(--white);letter-spacing:.2px}
.hero-copy{font-size:5.8px;line-height:1.9;color:var(--white)}
.btn{display:inline-flex;align-items:center;gap:3px;background:var(--green);color:var(--white);font:700 5.4px Roboto,sans-serif;text-transform:uppercase;padding:0 8px;height:17px;letter-spacing:.2px}
.btn i{width:5px;height:5px;border-radius:50%;background:var(--white);display:inline-block}
.hero-arrow{width:15px;height:15px;border-radius:50%;background:rgba(0,0,0,.45);border:1px solid rgba(255,255,255,.6)}
.scroll-down{width:22px;height:22px;border-radius:50%;background:var(--white);border:1px solid #ccc;left:246px}
/* headings */
.h2{font:700 13px Montserrat,sans-serif;color:var(--ink);letter-spacing:.2px}
.h2 .soft{color:#777;font-weight:600}
.h2--light{color:var(--white)}
.rule{display:block;width:22px;height:2px;background:var(--yellow);margin:4px auto 0}
.rule--left{margin-left:0}
.lead{font:700 5.6px/1.8 Roboto,sans-serif;color:var(--ink)}
.body{font-size:5px;line-height:2.1;color:#777}
/* framed photos */
.about-photo{border-radius:50%;background:radial-gradient(circle,#55799f 0%,#36567a 48%,#4f8a2a 70%,#5b9a2a 100%)}
.store-photo{border-radius:50%;background:radial-gradient(circle at 55% 45%,#c8d2da 0%,#6f8aa0 50%,#2f4a63 100%)}
.call{display:flex;align-items:center;gap:4px}
.call-dot{width:17px;height:17px;border-radius:50%;background:var(--yellow);display:flex;align-items:center;justify-content:center}
.call-dot svg{width:9px;height:9px;fill:var(--white)}
.call small{display:block;font-size:4.4px;color:#999}
.call b{font:700 7.5px Roboto,sans-serif}
/* quote */
.quote{background:var(--light)}
.quote-copy{font-size:6px;line-height:2.35;color:#666}
.input{position:absolute;background:var(--white);border:1px solid #e3e3e3;font-size:4.6px;color:#999;padding:9px 0 0 14px;height:23px;width:172px}
/* products */
.products{background:var(--green)}
.card{position:absolute;width:124px;height:98px}
.card-img{height:78px}
.card-label{position:absolute;left:6px;right:6px;top:68px;height:28px;background:var(--white);border-radius:2px;box-shadow:0 2px 4px rgba(0,0,0,.15);font:600 5.6px/28px Roboto,sans-serif;text-align:center}
.round-arrow{width:11px;height:11px;border-radius:50%;background:var(--white);display:flex;align-items:center;justify-content:center}
.round-arrow svg{width:6px;height:6px;stroke:var(--ink);fill:none;stroke-width:3}
/* reviews */
.review{position:absolute;width:163px;height:93px;background:var(--white);border-radius:14px;box-shadow:0 2px 6px rgba(0,0,0,.18)}
.avatar{position:absolute;left:-22px;top:23px;width:45px;height:45px;border-radius:50%;background:linear-gradient(160deg,#cfd5db,#8d98a3);border:2px solid var(--white)}
.quote-mark{position:absolute;left:41px;top:9px;font:700 20px/1 Georgia,serif;color:var(--yellow)}
.review p{position:absolute;left:41px;top:33px;width:112px;font-size:4.7px;line-height:2;color:#888;text-align:justify}
.review b{position:absolute;left:41px;top:65px;font-size:6px}
.stars{position:absolute;left:41px;top:74px;font-size:6px;color:var(--yellow);letter-spacing:.5px}
.side-arrow{stroke:#777;fill:none;stroke-width:1.6}
/* store */
.store{background:var(--cream)}
/* contact */
.col-title{font-size:7px;color:#555}
.detail{position:absolute;left:62px;display:flex;gap:12px;align-items:flex-start}
.detail svg{width:12px;height:12px;fill:var(--yellow);flex:none}
.detail .stroke{fill:none;stroke:var(--yellow);stroke-width:1.5}
.detail b{display:block;font-size:5.4px;font-weight:700;line-height:1.3;margin-bottom:2px}
.detail span{display:block;font-size:5.2px;line-height:1.3;color:#555}
.social{display:flex;gap:5px}
.social i{width:11px;height:11px;border-radius:50%;background:var(--green);display:block}
.field{position:absolute;background:var(--field);border:1px solid #dedede;height:17px;font-size:4.4px;color:#888;padding:6px 0 0 8px;width:99px}
/* footer */
.footer{background:var(--black)}
.foot-brand{font:600 10px/1.1 Montserrat,sans-serif;color:var(--white);width:100px}
.foot-col h4{font:700 5.4px Roboto,sans-serif;color:var(--white);margin-bottom:6px}
.foot-col p{font-size:4.8px;line-height:2.25;color:#ddd}
.badge-shape{background:linear-gradient(90deg,#3b2a7a,#5d48a8);border-radius:2px}
.copybar{background:#9c9c9c;color:var(--white);font-size:5px;text-align:center;line-height:15px}
/* distributors */
.dist-card{position:absolute;top:52px;width:67px;height:31px;background:var(--white);border-radius:3px;box-shadow:0 1px 4px rgba(0,0,0,.15);display:flex;align-items:center;justify-content:center;gap:3px;font:600 5.4px Roboto,sans-serif;color:#333}
.dist-card i{width:6px;height:6px;background:#333;display:block}
.dot{width:5px;height:5px;border-radius:50%;border:1px solid #555;display:inline-block;margin:0 1px}
/* contact band */
.band{position:absolute;left:54px;width:459px;height:95px;background:var(--green);color:var(--white);font-size:9.5px;line-height:1.15}
.band-deco{position:absolute;top:-10px;width:75px;height:125px;background:linear-gradient(90deg,#141414 0%,#2a2a2a 55%,#5b9a2a 100%);z-index:2}
.band-deco--right{background:linear-gradient(270deg,#141414 0%,#2a2a2a 55%,#5b9a2a 100%)}
.band-item{position:absolute;display:flex;align-items:center;gap:8px}
.band-item i{width:21px;height:21px;border-radius:50%;background:var(--white);display:flex;align-items:center;justify-content:center;flex:none}
.band-item svg{width:11px;height:11px;fill:var(--green)}
</style>
</head>
<body>
<svg width="0" height="0" style="position:absolute" aria-hidden="true">
  <defs>
    <symbol id="i-pin" viewBox="0 0 24 24"><path d="M12 2a7 7 0 0 0-7 7c0 5 7 13 7 13s7-8 7-13a7 7 0 0 0-7-7zm0 9.5a2.5 2.5 0 1 1 0-5 2.5 2.5 0 0 1 0 5z"/></symbol>
    <symbol id="i-phone" viewBox="0 0 24 24"><path d="M6.6 10.8a15 15 0 0 0 6.6 6.6l2.2-2.2a1 1 0 0 1 1-.25 11.4 11.4 0 0 0 3.6.6 1 1 0 0 1 1 1V20a1 1 0 0 1-1 1A17 17 0 0 1 3 4a1 1 0 0 1 1-1h3.5a1 1 0 0 1 1 1c0 1.25.2 2.45.6 3.6a1 1 0 0 1-.25 1z"/></symbol>
    <symbol id="i-mail" viewBox="0 0 24 24"><path d="M3 5h18v14H3zM3 5l9 7 9-7"/></symbol>
    <symbol id="i-left" viewBox="0 0 10 14"><path d="M8 1 2 7l6 6"/></symbol>
    <symbol id="i-right" viewBox="0 0 10 14"><path d="M2 1l6 6-6 6"/></symbol>
    <symbol id="i-search" viewBox="0 0 24 24"><circle cx="10" cy="10" r="6" fill="none" stroke="#1d1d1d" stroke-width="3"/><path d="M15 15l6 6" stroke="#1d1d1d" stroke-width="3"/></symbol>
  </defs>
</svg>

<!-- ================= CONCEPT A ================= -->
<main class="page page--a">
  <div class="sec topbar"><div class="topbar-strip"><span class="gold">Apply for Account</span><span class="gold">| Find Locations</span><span class="auth">Login | Register</span></div></div>
  <header class="sec header">
    <div class="brand"><span class="brand-box"></span><span class="brand-name">GRANITE VALLEY SUPPLY WORKS</span></div>
    <nav class="nav"><span>Home</span><span>About Us</span><span>Product</span><span>Shop</span><span>Catalog</span><span>Line Card</span><span>Promotions</span><span>Company Info</span><svg><use href="#i-search"/></svg></nav>
  </header>

  <section class="sec hero">
    <div class="hero-photo hero-photo--factory" role="img" aria-label="Engineer in hard hat at a laptop beside robotic arms on a factory floor"></div>
    <div class="hero-shade"></div>
    <p class="abs center welcome" style="top:48px">Welcome To</p>
    <h1 class="abs center hero-title" style="top:64px">GRANITE VALLEY SUPPLY WORKS</h1>
    <p class="abs center hero-copy" style="top:90px">Lorem ipsum dolor sit amet, consectetur adipiscing elit, sed<br>eiusmod tempor incididunt ut labore et dolore.</p>
    <div class="abs center" style="top:124px"><span class="btn">Get Started <i></i></span></div>
    <div class="abs hero-arrow" style="left:23px;top:100px"></div>
    <div class="abs hero-arrow" style="left:476px;top:100px"></div>
    <svg class="abs" style="left:0;bottom:0" width="514" height="40" viewBox="0 0 514 40"><path d="M0 20Q257-12 514 22V40H0z" fill="#f5b800"/><path d="M0 30Q257-6 514 26V40H0z" fill="#fff"/></svg>
    <div class="abs scroll-down" style="top:226px"></div>
  </section>

  <section class="sec" style="top:300px;height:235px">
    <div class="abs about-photo" role="img" aria-label="Machinist in hard hat operating a lathe, framed in a green gear" style="left:62px;top:12px;width:181px;height:181px"></div>
    <h2 class="abs h2" style="left:277px;top:26px">ABOUT <span class="soft">US</span><span class="rule rule--left"></span></h2>
    <p class="abs lead" style="left:277px;top:52px;width:180px">Lorem ipsum dolor sit amet, consectetur adipiscing elit, sed do eiusmod tempor incididunt ut labore.</p>
    <p class="abs body" style="left:277px;top:76px;width:180px">Sed ut perspiciatis unde omnis iste natus error sit voluptatem accusantium doloremque laudantium, totam rem aperiam, eaque ipsa quae ab illo inventore veritatis et quasi architecto beatae vitae dicta sunt explicabo ex ea commodo consequat.</p>
    <p class="abs body" style="left:277px;top:130px;width:180px">Duis aute irure dolor in reprehenderit in voluptate velit esse cillum dolore eu fugiat nulla pariatur. Excepteur sint occaecat.</p>
    <span class="abs btn" style="left:277px;top:163px">Learn More <i></i></span>
    <div class="abs call" style="left:360px;top:161px"><span class="call-dot"><svg><use href="#i-phone"/></svg></span><span><small>Schedule Now</small><b>+1-555-010-2040</b></span></div>
  </section>

  <section class="sec quote" style="top:535px;height:340px">
    <h2 class="abs center h2" style="top:25px">REQUEST A QUOTE <span class="soft">TODAY!</span></h2>
    <p class="abs center quote-copy" style="top:50px">With 35 years experience, our product knowledge is second to none. Our sales professionals have solutions to fit<br>any application. With an in house machinist to tailor fit your needs. All while keeping customer service<br>at the forefront of our business plan.</p>
    <p class="abs center quote-copy" style="top:100px;color:#444">Give us a call or complete our form below to schedule your free estimate.</p>
    <div class="input" style="left:79px;top:127px">First Name</div>
    <div class="input" style="left:264px;top:127px">Last Name</div>
    <div class="input" style="left:79px;top:162px">Contact Number</div>
    <div class="input" style="left:264px;top:162px">Email Address</div>
    <div class="input" style="left:79px;top:196px;width:357px;height:72px">Message</div>
    <div class="abs center" style="top:283px"><span class="btn">Submit Now <i></i></span></div>
  </section>

  <section class="sec products" style="top:865px;height:375px">
    <svg class="abs" style="left:0;top:0" width="514" height="40" viewBox="0 0 514 40"><path d="M0 0H514V4Q257 38 0 4z" fill="#f5b800"/><path d="M0 0H514Q257 28 0 0" fill="#f3f3f3"/></svg>
    <h2 class="abs center h2 h2--light" style="top:58px">OUR PRODUCTS<span class="rule"></span></h2>
    <div class="card" style="left:55px;top:101px"><div class="card-img" role="img" aria-label="Roller bearings stacked on a workbench" style="background:linear-gradient(135deg,#6e7b88,#b9c3cc 50%,#8a3a2a)"></div><div class="card-label">Bearing Pullers</div></div>
    <div class="card" style="left:195px;top:101px"><div class="card-img" role="img" aria-label="Conveyor line in a factory hall" style="background:linear-gradient(180deg,#9aa7b6,#3f5d8c 55%,#c9ced3)"></div><div class="card-label">Conveyor</div></div>
    <div class="card" style="left:334px;top:101px"><div class="card-img" role="img" aria-label="Blue belting roll on a machine" style="background:linear-gradient(135deg,#7d8a93,#2d6ab0 50%,#c0c6cb)"></div><div class="card-label">Belting</div></div>
    <div class="card" style="left:55px;top:220px"><div class="card-img" role="img" aria-label="Close-up of a mechanical coupling" style="background:linear-gradient(135deg,#5b5e63,#b76b2b 50%,#d2d2d2)"></div><div class="card-label">Couplings</div></div>
    <div class="card" style="left:195px;top:220px"><div class="card-img" role="img" aria-label="Row of blue electric motors" style="background:linear-gradient(135deg,#3f7fa3,#7fc0d8 50%,#546b7a)"></div><div class="card-label">Motors</div></div>
    <div class="card" style="left:334px;top:220px"><div class="card-img" role="img" aria-label="Coiled wire mesh belting" style="background:linear-gradient(135deg,#4c4236,#8c7b62 50%,#5a5044)"></div><div class="card-label">Belting Wire</div></div>
    <div class="abs round-arrow" style="left:21px;top:207px"><svg><use href="#i-left"/></svg></div>
    <div class="abs round-arrow" style="left:482px;top:207px"><svg><use href="#i-right"/></svg></div>
    <svg class="abs" style="left:0;bottom:0" width="514" height="40" viewBox="0 0 514 40"><path d="M0 24Q257-8 514 26V40H0z" fill="#f5b800"/><path d="M0 32Q257-2 514 30V40H0z" fill="#fff"/></svg>
  </section>

  <section class="sec" style="top:1240px;height:180px">
    <h2 class="abs center h2" style="top:12px;left:-8px">CUSTOMER <span class="soft">REVIEWS</span><span class="rule"></span></h2>
    <div class="review" style="left:80px;top:47px"><div class="avatar" role="img" aria-label="Customer portrait"></div><span class="quote-mark">&ldquo;</span><p>Lorem ipsum dolor sit amet, consectetur adipiscing elit, sed do eiusmod tempor incididunt ut labore et dolore.</p><b>Marcus Dell</b><span class="stars">★★★★★</span></div>
    <div class="review" style="left:285px;top:47px"><div class="avatar" role="img" aria-label="Customer portrait"></div><span class="quote-mark">&ldquo;</span><p>Lorem ipsum dolor sit amet, consectetur adipiscing elit, sed do eiusmod tempor incididunt ut labore et dolore</p><b>Renee Ortiz</b><span class="stars">★★★★★</span></div>
    <svg class="abs side-arrow" style="left:30px;top:86px" width="10" height="14" viewBox="0 0 10 14"><path d="M8 1 2 7l6 6"/></svg>
    <svg class="abs side-arrow" style="left:474px;top:86px" width="10" height="14" viewBox="0 0 10 14"><path d="M2 1l6 6-6 6"/></svg>
  </section>

  <section class="sec store" style="top:1420px;height:230px">
    <h2 class="abs h2" style="left:62px;top:43px">OUR <span class="soft" style="color:var(--ink)">STORE</span><span class="rule rule--left"></span></h2>
    <p class="abs body" style="left:62px;top:67px;width:190px">Lorem ipsum dolor sit amet, consectetur adipiscing elit, sed do eiusmod tempor incididunt ut labore et dolore magna aliqua. Ut enim ad minim veniam, quis nostrud exercitation ullamco laboris nisi ut aliquip ex ea commodo consequat.</p>
    <p class="abs body" style="left:62px;top:116px;width:190px">Duis aute irure dolor in reprehenderit in voluptate velit esse cillum dolore eu fugiat nulla pariatur. Excepteur sint occaecat cupidatat non proident, sunt in culpa qui officia deserunt mollit anim id est laborum.</p>
    <span class="abs btn" style="left:62px;top:163px">Contact Now <i></i></span>
    <div class="abs store-photo" role="img" aria-label="Gloved hands working on technical drawings, framed in a gear shape" style="left:276px;top:25px;width:181px;height:181px"></div>
  </section>

  <section class="sec" style="top:1650px;height:240px">
    <h2 class="abs center h2" style="top:36px">CONTACT <span class="soft">US</span><span class="rule"></span></h2>
    <p class="abs col-title" style="left:62px;top:72px">Contact Details</p>
    <p class="abs col-title" style="left:243px;top:72px">Get In Touch</p>
    <div class="detail" style="top:92px"><svg><use href="#i-pin"/></svg><div><b>ADDRESS</b><span>1280 Quarry Rd, Millbrook, VT 05601</span></div></div>
    <div class="detail" style="top:124px"><svg><use href="#i-phone"/></svg><div><b>PHONE NUMBER</b><span>555-018-4471</span></div></div>
    <div class="detail" style="top:152px"><svg class="stroke"><use href="#i-mail"/></svg><div><b>EMAIL</b><span>info@granitevalleysupply.com</span></div></div>
    <div class="abs social" style="left:62px;top:186px"><i></i><i></i></div>
    <div class="field" style="left:243px;top:97px">Name</div>
    <div class="field" style="left:354px;top:97px">Phone Number</div>
    <div class="field" style="left:243px;top:120px">Email Address</div>
    <div class="field" style="left:354px;top:120px">Subject</div>
    <div class="field" style="left:243px;top:143px;width:210px;height:34px;padding-top:12px">Message</div>
    <span class="abs btn" style="left:243px;top:189px;padding:0 10px">Submit</span>
  </section>

  <section class="sec footer" style="top:1870px;height:199px">
    <svg class="abs" style="left:0;top:0" width="514" height="42" viewBox="0 0 514 42"><path d="M0 0H514V8Q257 48 0 14z" fill="#f5b800"/><path d="M0 0H514V0Q257 38 0 6z" fill="#fff"/></svg>
    <div class="abs" style="left:60px;top:68px;display:flex;align-items:center;gap:4px"><span style="width:12px;height:22px;background:#fff"></span><span class="foot-brand">GRANITE VALLEY SUPPLY WORKS</span></div>
    <div class="abs badge-shape" role="img" aria-label="Certification badge" style="left:61px;top:112px;width:97px;height:36px"></div>
    <div class="abs foot-col" style="left:198px;top:68px"><h4>QUICK LINKS</h4><p>Home<br>About Us<br>Product<br>Shop<br>Catalog<br>Line Card<br>Promotions<br>Company Info</p></div>
    <div class="abs foot-col" style="left:277px;top:68px"><h4>ABOUT COMPANY</h4><p>Privacy Policy<br>Terms of Service<br>Site Map<br>Imprint<br>Terms And Conditions</p></div>
    <div class="abs foot-col" style="left:376px;top:68px"><h4>CONTACT US</h4><p><b>Phone</b><br>555-018-4472<br><b>Email</b><br>info@granitevalleysupply.com<br><b>Location</b><br>1280 Quarry Rd, Millbrook,<br>VT 05601</p></div>
    <div class="abs copybar" style="left:0;bottom:0;width:514px;height:15px">2024 Copyright - Granite Valley Supply Works | All Rights Reserved</div>
  </section>
</main>

<!-- ================= CONCEPT B ================= -->
<main class="page page--b">
  <div class="sec topbar"><div class="topbar-strip"><span class="gold">Apply for Account</span><span class="gold">| Find Locations</span><span class="auth">Login | Register</span></div></div>
  <header class="sec header">
    <div class="brand"><span class="brand-box"></span><span class="brand-name">GRANITE VALLEY SUPPLY WORKS</span></div>
    <nav class="nav"><span>Home</span><span>About Us</span><span>Product</span><span>Shop</span><span>Catalog</span><span>Line Card</span><span>Promotions</span><span>Company Info</span><svg><use href="#i-search"/></svg></nav>
  </header>

  <section class="sec hero">
    <div class="hero-photo hero-photo--warehouse" role="img" aria-label="Long warehouse aisle lined with stacked cartons"></div>
    <div class="hero-shade"></div>
    <p class="abs center welcome" style="top:60px">Welcome To</p>
    <h1 class="abs center hero-title" style="top:76px">GRANITE VALLEY SUPPLY WORKS</h1>
    <p class="abs center hero-copy" style="top:104px;font-size:7.5px">We Keep Plants Running</p>
    <div class="abs center" style="top:133px"><span class="btn">Get Started <i></i></span></div>
    <svg class="abs" style="left:45px;top:86px" width="12" height="20" viewBox="0 0 10 14"><path d="M8 1 2 7l6 6" fill="none" stroke="#fff" stroke-width="2"/></svg>
    <svg class="abs" style="left:457px;top:86px" width="12" height="20" viewBox="0 0 10 14"><path d="M2 1l6 6-6 6" fill="none" stroke="#fff" stroke-width="2"/></svg>
    <svg class="abs" style="left:0;bottom:0" width="514" height="40" viewBox="0 0 514 40"><path d="M0 20Q257-12 514 22V40H0z" fill="#f5b800"/><path d="M0 30Q257-6 514 26V40H0z" fill="#fff"/></svg>
    <div class="abs scroll-down" style="top:226px"></div>
  </section>

  <section class="sec" style="top:300px;height:117px">
    <h2 class="abs center h2" style="top:14px"><span class="soft">OUR</span> DISTRIBUTORS<span class="rule"></span></h2>
    <div class="dist-card" style="left:65px"><i></i>Northwind</div>
    <div class="dist-card" style="left:146px"><i></i>Ironleaf</div>
    <div class="dist-card" style="left:227px"><i></i>Boltline</div>
    <div class="dist-card" style="left:308px"><i></i>Keystone</div>
    <div class="dist-card" style="left:389px"><i></i>Axial</div>
    <div class="abs center" style="top:98px"><span class="dot"></span><span class="dot" style="background:var(--yellow);border-color:var(--yellow)"></span><span class="dot"></span></div>
  </section>

  <section class="sec" style="top:417px;height:235px">
    <div class="abs about-photo" role="img" aria-label="Machinist in hard hat operating a lathe, framed in a green gear" style="left:62px;top:12px;width:181px;height:181px"></div>
    <h2 class="abs h2" style="left:277px;top:26px">ABOUT <span class="soft">US</span><span class="rule rule--left"></span></h2>
    <p class="abs lead" style="left:277px;top:52px;width:180px">Lorem ipsum dolor sit amet, consectetur adipiscing elit, sed do eiusmod tempor incididunt ut labore.</p>
    <p class="abs body" style="left:277px;top:76px;width:180px">Sed ut perspiciatis unde omnis iste natus error sit voluptatem accusantium doloremque laudantium, totam rem aperiam, eaque ipsa quae ab illo inventore veritatis et quasi architecto beatae vitae dicta sunt explicabo ex ea commodo consequat.</p>
    <p class="abs body" style="left:277px;top:130px;width:180px">Duis aute irure dolor in reprehenderit in voluptate velit esse cillum dolore eu fugiat nulla pariatur. Excepteur sint occaecat.</p>
    <span class="abs btn" style="left:277px;top:163px">Learn More <i></i></span>
    <div class="abs call" style="left:360px;top:161px"><span class="call-dot"><svg><use href="#i-phone"/></svg></span><span><small>Schedule Now</small><b>+1-555-010-2040</b></span></div>
  </section>

  <section class="sec quote" style="top:652px;height:340px">
    <h2 class="abs center h2" style="top:25px">REQUEST A QUOTE <span class="soft">TODAY!</span></h2>
    <p class="abs center quote-copy" style="top:50px">With 35 years experience, our product knowledge is second to none. Our sales professionals have solutions to fit<br>any application. With an in house machinist to tailor fit your needs. All while keeping customer service<br>at the forefront of our business plan.</p>
    <p class="abs center quote-copy" style="top:100px;color:#444">Give us a call or complete our form below to schedule your free estimate.</p>
    <div class="input" style="left:79px;top:127px">First Name</div>
    <div class="input" style="left:264px;top:127px">Last Name</div>
    <div class="input" style="left:79px;top:162px">Contact Number</div>
    <div class="input" style="left:264px;top:162px">Email Address</div>
    <div class="input" style="left:79px;top:196px;width:357px;height:72px">Message</div>
    <div class="abs center" style="top:283px"><span class="btn">Submit Now <i></i></span></div>
  </section>

  <section class="sec products" style="top:982px;height:375px">
    <svg class="abs" style="left:0;top:0" width="514" height="40" viewBox="0 0 514 40"><path d="M0 0H514V4Q257 38 0 4z" fill="#f5b800"/><path d="M0 0H514Q257 28 0 0" fill="#f3f3f3"/></svg>
    <h2 class="abs center h2 h2--light" style="top:58px">OUR PRODUCTS<span class="rule"></span></h2>
    <div class="card" style="left:55px;top:101px"><div class="card-img" role="img" aria-label="Roller bearings stacked on a workbench" style="background:linear-gradient(135deg,#3d6aa8,#a9c3e0 50%,#2f4f80)"></div><div class="card-label">Bearing Pullers</div></div>
    <div class="card" style="left:195px;top:101px"><div class="card-img" role="img" aria-label="Conveyor line in a factory hall" style="background:linear-gradient(180deg,#9aa7b6,#3f5d8c 55%,#c9ced3)"></div><div class="card-label">Conveyor</div></div>
    <div class="card" style="left:334px;top:101px"><div class="card-img" role="img" aria-label="Blue belting roll on a machine" style="background:linear-gradient(135deg,#7d8a93,#2d6ab0 50%,#c0c6cb)"></div><div class="card-label">Belting</div></div>
    <div class="card" style="left:55px;top:220px"><div class="card-img" role="img" aria-label="Close-up of a mechanical coupling" style="background:linear-gradient(135deg,#5b5e63,#b76b2b 50%,#d2d2d2)"></div><div class="card-label">Couplings</div></div>
    <div class="card" style="left:195px;top:220px"><div class="card-img" role="img" aria-label="Row of blue electric motors" style="background:linear-gradient(135deg,#3f7fa3,#7fc0d8 50%,#546b7a)"></div><div class="card-label">Motors</div></div>
    <div class="card" style="left:334px;top:220px"><div class="card-img" role="img" aria-label="Coiled wire mesh belting" style="background:linear-gradient(135deg,#4c4236,#8c7b62 50%,#5a5044)"></div><div class="card-label">Belting Wire</div></div>
    <div class="abs round-arrow" style="left:21px;top:207px"><svg><use href="#i-left"/></svg></div>
    <div class="abs round-arrow" style="left:482px;top:207px"><svg><use href="#i-right"/></svg></div>
    <svg class="abs" style="left:0;bottom:0" width="514" height="40" viewBox="0 0 514 40"><path d="M0 24Q257-8 514 26V40H0z" fill="#f5b800"/><path d="M0 32Q257-2 514 30V40H0z" fill="#fff"/></svg>
  </section>

  <section class="sec" style="top:1357px;height:180px">
    <h2 class="abs center h2" style="top:12px;left:-8px">CUSTOMER <span class="soft">REVIEWS</span><span class="rule"></span></h2>
    <div class="review" style="left:80px;top:47px"><div class="avatar" role="img" aria-label="Customer portrait"></div><span class="quote-mark">&ldquo;</span><p>Lorem ipsum dolor sit amet, consectetur adipiscing elit, sed do eiusmod tempor incididunt ut labore et dolore.</p><b>Marcus Dell</b><span class="stars">★★★★★</span></div>
    <div class="review" style="left:285px;top:47px"><div class="avatar" role="img" aria-label="Customer portrait"></div><span class="quote-mark">&ldquo;</span><p>Lorem ipsum dolor sit amet, consectetur adipiscing elit, sed do eiusmod tempor incididunt ut labore et dolore</p><b>Renee Ortiz</b><span class="stars">★★★★★</span></div>
    <svg class="abs side-arrow" style="left:30px;top:86px" width="10" height="14" viewBox="0 0 10 14"><path d="M8 1 2 7l6 6"/></svg>
    <svg class="abs side-arrow" style="left:474px;top:86px" width="10" height="14" viewBox="0 0 10 14"><path d="M2 1l6 6-6 6"/></svg>
  </section>

  <section class="sec store" style="top:1537px;height:230px">
    <h2 class="abs h2" style="left:62px;top:43px">OUR <span class="soft" style="color:var(--ink)">STORE</span><span class="rule rule--left"></span></h2>
    <p class="abs body" style="left:62px;top:67px;width:190px">Lorem ipsum dolor sit amet, consectetur adipiscing elit, sed do eiusmod tempor incididunt ut labore et dolore magna aliqua. Ut enim ad minim veniam, quis nostrud exercitation ullamco laboris nisi ut aliquip ex ea commodo consequat.</p>
    <p class="abs body" style="left:62px;top:116px;width:190px">Duis aute irure dolor in reprehenderit in voluptate velit esse cillum dolore eu fugiat nulla pariatur. Excepteur sint occaecat cupidatat non proident, sunt in culpa qui officia deserunt mollit anim id est laborum.</p>
    <span class="abs btn" style="left:62px;top:163px">Contact Now <i></i></span>
    <div class="abs store-photo" role="img" aria-label="Gloved hands working on technical drawings, framed in a gear shape" style="left:276px;top:25px;width:181px;height:181px"></div>
  </section>

  <section class="sec" style="top:1767px;height:230px">
    <h2 class="abs center h2" style="top:30px">CONTACT <span class="soft">US</span><span class="rule"></span></h2>
    <p class="abs col-title" style="left:62px;top:66px">Contact Details</p>
    <p class="abs col-title" style="left:243px;top:66px">Get In Touch</p>
    <div class="detail" style="top:86px"><svg><use href="#i-pin"/></svg><div><b>ADDRESS</b><span>1280 Quarry Rd, Millbrook, VT 05601</span></div></div>
    <div class="detail" style="top:118px"><svg><use href="#i-phone"/></svg><div><b>PHONE NUMBER</b><span>555-018-4471</span></div></div>
    <div class="detail" style="top:146px"><svg class="stroke"><use href="#i-mail"/></svg><div><b>EMAIL</b><span>info@granitevalleysupply.com</span></div></div>
    <div class="abs social" style="left:62px;top:180px"><i></i><i></i></div>
    <div class="field" style="left:243px;top:91px">Name</div>
    <div class="field" style="left:354px;top:91px">Phone Number</div>
    <div class="field" style="left:243px;top:114px">Email Address</div>
    <div class="field" style="left:354px;top:114px">Subject</div>
    <div class="field" style="left:243px;top:137px;width:210px;height:34px;padding-top:12px">Message</div>
    <span class="abs btn" style="left:243px;top:183px;padding:0 10px">Submit</span>
  </section>

  <section class="sec" style="top:1997px;height:128px">
    <div class="band" style="top:14px">
      <div class="band-item" style="left:62px;top:14px"><i><svg><use href="#i-pin"/></svg></i><span>1280 Quarry Rd, Millbrook,<br>VT 05601</span></div>
      <div class="band-item" style="left:248px;top:16px"><i><svg><use href="#i-phone"/></svg></i><span>555-018-4472</span></div>
      <div class="band-item" style="left:62px;top:58px"><i><svg><use href="#i-phone"/></svg></i><span>555-018-4471</span></div>
      <div class="band-item" style="left:248px;top:58px"><i><svg style="fill:none;stroke:var(--green);stroke-width:2"><use href="#i-mail"/></svg></i><span>info@granitevalleysupply.com</span></div>
    </div>
    <div class="band-deco" role="img" aria-label="Decorative gear artwork" style="left:2px;top:4px"></div>
    <div class="band-deco band-deco--right" role="img" aria-label="Decorative gear artwork" style="left:437px;top:4px"></div>
  </section>

  <section class="sec footer" style="top:2115px;height:217px">
    <svg class="abs" style="left:0;top:0" width="514" height="60" viewBox="0 0 514 60"><path d="M0 0H514V28Q257 68 0 28z" fill="#f5b800"/><path d="M0 0H514V22Q257 60 0 22z" fill="#fff"/></svg>
    <div class="abs" style="left:205px;top:95px;display:flex;align-items:center;gap:4px"><span style="width:12px;height:22px;background:#fff"></span><span class="foot-brand">GRANITE VALLEY SUPPLY WORKS</span></div>
    <div class="abs" style="left:125px;top:141px;display:flex;gap:32px;font-size:5.4px;color:#fff"><span>Home</span><span>About Us</span><span>Our Services</span><span>Testimonials</span><span>Contact Us</span></div>
    <p class="abs" style="left:130px;top:168px;font-size:4.8px;color:#ddd">(C) Copyright 2024 | All Rights Reserved</p>
    <div class="abs badge-shape" role="img" aria-label="Certification badge" style="left:281px;top:164px;width:43px;height:14px"></div>
    <div class="abs" style="left:337px;top:165px;display:flex;gap:3px"><i style="width:12px;height:12px;border-radius:50%;background:var(--yellow);display:block"></i><i style="width:12px;height:12px;border-radius:50%;background:var(--yellow);display:block"></i><i style="width:12px;height:12px;border-radius:50%;background:var(--yellow);display:block"></i></div>
  </section>
</main>
</body>
</html>
```